依頼詳細

開催期間の告知とブランド名・ブランドイメージ(古典洋菓子を新しいスタイルと変わらぬおいしさで。商品は花々のようにカラフルで華やかさと品のある中に他には無い大人の遊び心のような商品を展開)をお客様に認知していただける様なブランドイメージを反映したデザイン性のあるポスターを希望します。(出来ればハイブランドの化粧品メーカーやアパレルメーカーのイメージポスターのようなシックな感じと遊び心を兼ね備えたイメージで)
記載項目
株式会社ロワ・ベルネ
0561-84-2957
希望イメージ
シンプル 複雑
単色 カラフル
暗い 明るい
日常 高級
遊び心 厳粛
未来的 伝統的
女性的 男性的
希望する色
春らしい色味で
納品ファイル
• イラストレーター形式 (.ai)
補足説明
依頼公開後の追記内容
ロゴAIデータ追加させていただきます。
■ 選んだ理由

今回は期間限定の催事イベント販売の告知ポスターということもあり、期間の告知・商品が分かりやすい事・春のイベントを強調する事選考のポイントとさせて頂きました。
tako-run様のご提案はトータル的なバランスが良かったので、今回決定させて頂きました。

■ 提案者全員のお礼・コメント

この度は弊社洋菓子店催事告示ポスターに、ご参加ご提案を頂きまして誠にありがとうございました。
皆様とても素敵なデザインで甲乙つけ難く選考はとても悩みました。
また、近々に別件にて夏商品の告知ポスターを依頼させて頂く予定でございます。
その折には、皆様ご参加頂けますようよろしくお願い申し上げます。

```html
<!DOCTYPE html>
<html lang="ja">
<head>
<meta charset="utf-8">
<title>PÂTISSERIE LOMIELLE 春の催事ポスター</title>
<link rel="stylesheet" href="https://fonts.googleapis.com/css2?family=Josefin+Sans:wght@300;400&family=Noto+Sans+JP:wght@400;500&display=swap">
<style>
  :root {
    --paper: #ffffff;
    --ink: #2b2b2b;
    --accent: #2a8fb8;
    --film: #111111;
    --dot-orange: #f6c9a0;
    --dot-green: #bfe0b0;
    --dot-pink: #f1c6cf;
    --dot-mint: #cde9d6;
  }
  html, body { margin: 0; padding: 0; overflow: hidden; background: var(--paper); }
  .poster {
    position: relative;
    width: 849px; height: 1200px;
    overflow: hidden;
    background: var(--paper);
    font-family: "Noto Sans JP", sans-serif;
    color: var(--ink);
  }
  .dot-field {
    position: absolute; left: 0; top: 0; width: 497px; height: 1200px;
    background:
      linear-gradient(200deg, rgba(246,201,160,.55) 0%, rgba(255,255,255,0) 40%),
      linear-gradient(160deg, rgba(191,224,176,.5) 20%, rgba(255,255,255,0) 60%),
      linear-gradient(20deg, rgba(241,198,207,.55) 0%, rgba(205,233,214,.4) 40%, rgba(255,255,255,0) 70%);
  }
  .brand-block {
    position: absolute; left: 50px; top: 500px;
    width: 430px; height: 190px;
    background: var(--paper);
  }
  .brand-mark {
    position: absolute; left: 10px; top: 40px;
    width: 108px; height: 108px; border-radius: 50%;
    border: 2px solid var(--ink); box-sizing: border-box;
  }
  .brand-name {
    position: absolute; left: 140px; top: 42px;
    font-family: "Josefin Sans", sans-serif; font-weight: 300;
    color: var(--ink); line-height: 1;
  }
  .brand-name .sub { display: block; font-size: 24px; letter-spacing: 3px; margin-bottom: 10px; }
  .brand-name .main { display: block; font-size: 52px; letter-spacing: 4px; }
  .dates {
    position: absolute; left: 330px; top: 710px;
    font-family: "Josefin Sans", sans-serif; font-weight: 300;
    font-size: 30px; letter-spacing: 2px; color: var(--ink);
  }
  .contact {
    position: absolute; left: 78px; top: 1055px;
    font-size: 21px; line-height: 1.3; letter-spacing: 1px;
    background: var(--paper); padding: 2px 6px;
  }
  .contact p { margin: 0; }
  .film-strip {
    position: absolute; left: 497px; top: 0; width: 331px; height: 1200px;
    background: var(--film);
  }
  .frame {
    position: absolute; left: 14px; width: 303px;
  }
  .frame-1 { top: 18px;  height: 250px; background: linear-gradient(160deg,#f3f1ee,#cfb9a6 60%,#5a3b2c); }
  .frame-2 { top: 285px; height: 205px; background: linear-gradient(180deg,#fafafa,#e9e6e3 60%,#d6b78c); }
  .frame-3 { top: 507px; height: 210px; background: linear-gradient(150deg,#fbf7f1,#d8b27a 55%,#6a3d22); }
  .frame-4 { top: 734px; height: 215px; background: linear-gradient(170deg,#f7f4f2,#eec0c4 55%,#d97d86); }
  .frame-5 { top: 966px; height: 216px; background: linear-gradient(160deg,#efe7dc,#e79a88 50%,#8a5a3c); }
</style>
</head>
<body>
<main class="poster">
  <div class="dot-field" role="img" aria-label="春色の水玉模様（オレンジ・グリーン・ピンク）"></div>

  <section class="brand-block">
    <div class="brand-mark"></div>
    <h1 class="brand-name"><span class="sub">PÂTISSERIE</span><span class="main">LOMIELLE</span></h1>
  </section>

  <p class="dates">3/24〜4/13</p>

  <footer class="contact">
    <p>株式会社ロワ・ベルネ</p>
    <p>0561-84-2957</p>
    <p>ベーシックプラン</p>
  </footer>

  <aside class="film-strip">
    <div class="frame frame-1" role="img" aria-label="チョコレートとカラフルなトッピングのプチガトー"></div>
    <div class="frame frame-2" role="img" aria-label="白いドーム型ムースケーキ"></div>
    <div class="frame frame-3" role="img" aria-label="層になったチョコレートのカットケーキ"></div>
    <div class="frame frame-4" role="img" aria-label="ピンクのロールケーキ"></div>
    <div class="frame frame-5" role="img" aria-label="色とりどりのタルトの詰め合わせ"></div>
  </aside>
</main>
</body>
</html>
```